Curl Radiant through and through. Hair stylist that specializes in extensions.

I am Marisol I am a hair stylist and I would like a website designed for my hair business.

I currently book clients via my profile on trimnook.example/marisolbrantley

I need a professional website ( curlradiantthroughandthrough.example ) to display photos and prices for services offered.

I would like to have a home page with a brief bio, Image with logo and testimonials at the bottom, and a header with tab that include: menu of services, gallery,and FAQs.

On the "Services" page, I'm not interested in photos on this page. Just the name of the service, brief description, and pricing. I would also like to have, on this page, "Appointment Request" with fields that include: Name, service requested, desired time frame (morning, afternoon, evening), and contact number and email

On the "Gallery" page, I would like pictures only, but arranged and/or presented in a creative way...

Target Market(s)

Women ages 25-55 who interested in hair extension services.

Industry/Entity Type

Hair And Beauty

Coding

Number of Pages Required

5+ page

Font styles to use
Sans Serif

Requirements
Must have
• Must include tabs that include, Menu of services offered, a quick fund link to pay deposits with ease, location, contact information, photo gallery, and policy/faqs.
Nice to have
• If possible i would like to stream music with the ability to be silenced. I would like a neutral color palette tans and beige.
Should not have
• stock images

```html
<!DOCTYPE html>
<html lang="en">
<head>
<meta charset="utf-8">
<title>Curl Radiant through and through</title>
<link rel="stylesheet" href="https://fonts.googleapis.com/css2?family=Montserrat:wght@400;600;700&family=Open+Sans:wght@400;600;700&family=Lora:wght@400;700&display=swap">
<style>
:root{
  --gold:#e2a95c;
  --gold-dark:#d69a4a;
  --ink:#222;
  --text:#6d6d6d;
  --topbar:#23252a;
  --header:#363940;
  --nav:#2a2c31;
  --about-bg:#efefef;
  --panel:#1f2024;
  --testi:#333437;
  --footer:#25282c;
  --footer-text:#8b8e93;
  --white:#fff;
}
*{box-sizing:border-box;margin:0;padding:0}
html,body{width:1200px;height:2866px;overflow:hidden}
body{position:relative;background:var(--white);font-family:"Open Sans",Arial,sans-serif;color:var(--ink)}
.abs{position:absolute}

/* top bar */
.topbar{left:0;top:0;width:1200px;height:31px;background:var(--topbar)}
.topbar ul{position:absolute;right:132px;top:0;display:flex;gap:30px;list-style:none;align-items:center;height:31px;font-size:10px;color:#ddd}
.topbar .login{background:var(--gold);color:#fff;padding:2px 14px}

/* header */
.header{left:0;top:31px;width:1200px;height:99px;background:var(--header)}
.brand{position:absolute;left:132px;top:26px;color:#fff;font-family:"Montserrat",sans-serif}
.brand .name{font-size:34px;font-weight:700;letter-spacing:4px;line-height:36px}
.brand .tag{font-size:7px;font-weight:600;letter-spacing:.8px}
.search{position:absolute;left:793px;top:36px;width:273px;height:29px;display:flex}
.search .field{flex:1;background:#fff}
.search .btn{width:62px;background:var(--gold);color:#fff;font-size:10px;font-weight:700;display:flex;align-items:center;justify-content:center}

/* nav */
.nav{left:0;top:130px;width:1200px;height:32px;background:var(--nav)}
.nav ul{position:absolute;left:142px;top:0;height:32px;display:flex;list-style:none;align-items:center;font-family:"Montserrat",sans-serif;font-size:11px;color:#fff;letter-spacing:.4px}
.nav li{margin-right:60px}
.nav li.active{color:var(--gold)}

/* hero */
.hero{left:0;top:162px;width:1200px;height:367px;background:radial-gradient(ellipse 260px 340px at 720px 180px,#8b7564 0%,#5a4a40 45%,#2e2724 100%)}
.hero .rule{position:absolute;left:132px;top:134px;width:90px;height:2px;background:#6d625b}
.hero .caption{position:absolute;left:132px;top:148px;width:499px;height:72px;background:rgba(40,36,34,.85);color:#fff;font-family:"Montserrat",sans-serif;font-weight:700;font-size:34px;line-height:72px;padding-left:50px}
.hero .arrow{position:absolute;top:279px;width:41px;height:41px;background:#2a2a2a;display:flex;align-items:center;justify-content:center}
.hours{position:absolute;left:898px;top:75px;width:166px;height:229px;background:#2b2c2f;border:2px solid #4a4b4e;padding:4px 8px}
.hours h3{color:#fff;font-family:"Montserrat",sans-serif;font-weight:400;font-size:12px;text-align:center;margin:6px 0 8px}
.hours table{width:100%;border-collapse:collapse;font-size:9px;color:#fff}
.hours td{background:var(--panel);height:24px;padding:0 8px;border-bottom:3px solid #2b2c2f;font-weight:600}
.hours td+td{text-align:right;font-weight:400}
.hours tr.today td:first-child{color:#9d8cd6}
.hours tr.closed td{background:#3a3b3e;color:#888;font-weight:400}

/* section headings */
.section-title{display:flex;align-items:center;justify-content:center;gap:14px;width:1200px;left:0;font-family:"Montserrat",sans-serif;font-weight:600;font-size:27px;color:var(--gold);letter-spacing:1px}
.btn-gold{background:var(--gold);color:#fff;display:flex;align-items:center;justify-content:center;font-size:15px}

/* about */
.about{left:132px;top:569px;width:934px;height:408px;background:var(--about-bg)}
.about h2{position:absolute;left:23px;top:104px;font-family:"Lora",serif;font-weight:400;font-size:21px;letter-spacing:.6px;color:#1f1f1f}
.about p{position:absolute;left:25px;top:141px;width:620px;font-size:11px;line-height:22px;color:var(--text)}
.portrait{left:668px;top:88px;width:240px;height:240px}

/* gallery */
.photo{position:absolute}

/* our work */
.tabs{left:0;top:1868px;width:1200px;display:flex;justify-content:center;gap:34px;font-family:"Montserrat",sans-serif;font-size:11px;font-weight:600;letter-spacing:1px;color:#222}
.tabs .active{color:var(--gold);border-bottom:2px solid var(--gold);padding-bottom:8px}
.work-card{top:1919px;width:216px;height:177px}
.service-box{left:132px;top:1919px;width:216px;height:177px;background:#1f1d1c;color:#fff;text-align:center;padding-top:34px}
.service-box h4{font-family:"Lora",serif;font-size:14px;text-decoration:underline;letter-spacing:.5px}
.service-box p{font-size:11px;line-height:16px;margin:6px 22px 0;font-weight:600}
.service-box .book{display:inline-block;margin-top:10px;border:1px solid #fff;padding:4px 12px;font-size:14px}

/* testimonial */
.testimonial{left:132px;top:2136px;width:934px;height:450px;background:linear-gradient(180deg,#2e2f31,#3b3c3e 50%,#303133)}
.testimonial .lead{position:absolute;left:0;width:934px;top:106px;text-align:center;font-family:"Lora",serif;color:#fff;font-size:14px}
.quote{position:absolute;left:277px;top:188px;width:380px;height:120px;border:1px solid #b98c52;color:#fff;font-family:"Lora",serif;font-size:12.5px;line-height:22px;text-align:center;padding:13px 22px}
.author{position:absolute;left:398px;top:334px;display:flex;align-items:center;gap:22px;color:#fff;font-family:"Lora",serif;font-size:13px}
.avatar{width:60px;height:60px;border-radius:50%;background:#e8dcd0;border:3px solid #fff}
.dots{position:absolute;left:449px;top:415px;display:flex;gap:8px}
.dots span{width:10px;height:10px;border-radius:50%;background:#fff}
.dots span:first-child{background:var(--gold)}

/* footer */
.footer{left:0;top:2586px;width:1200px;height:280px;background:var(--footer);color:var(--footer-text);font-size:10px}
.footer h5{position:absolute;top:20px;font-family:"Lora",serif;font-weight:400;font-size:13px;color:#fff}
.footer h5.gold{color:var(--gold)}
.footer ul{list-style:none;position:absolute}
.contact li{display:flex;gap:14px;align-items:flex-start;margin-bottom:16px;width:200px;line-height:14px}
.ic{flex:none;width:24px;height:24px;border-radius:50%;background:#474a4f;display:flex;align-items:center;justify-content:center}
.ic.pin{background:var(--gold)}
.social li{display:flex;align-items:center;gap:14px;height:24px;margin-bottom:16px}
.media li{margin-bottom:9px}
.copyright{position:absolute;left:132px;top:243px;color:#ddd;font-size:10px}
.pay{position:absolute;top:235px;height:28px;width:42px;background:#fff;border-radius:2px;display:flex;align-items:center;justify-content:center;font-family:"Open Sans",sans-serif;font-size:7px;font-weight:700;color:#444}
</style>
</head>
<body>

<svg width="0" height="0" style="position:absolute">
  <defs>
    <symbol id="scissors" viewBox="0 0 40 40">
      <circle cx="10" cy="31" r="5" fill="none" stroke="#333" stroke-width="2.5"/>
      <circle cx="30" cy="31" r="5" fill="none" stroke="#333" stroke-width="2.5"/>
      <line x1="13" y1="27" x2="32" y2="4" stroke="#333" stroke-width="3"/>
      <line x1="27" y1="27" x2="8" y2="4" stroke="#333" stroke-width="3"/>
    </symbol>
    <symbol id="scissors-light" viewBox="0 0 40 40">
      <circle cx="10" cy="31" r="5" fill="none" stroke="#fff" stroke-width="2.5"/>
      <circle cx="30" cy="31" r="5" fill="none" stroke="#fff" stroke-width="2.5"/>
      <line x1="13" y1="27" x2="32" y2="4" stroke="#fff" stroke-width="3"/>
      <line x1="27" y1="27" x2="8" y2="4" stroke="#fff" stroke-width="3"/>
    </symbol>
  </defs>
</svg>

<!-- top bar -->
<div class="abs topbar">
  <ul>
    <li>Default welcome msg!</li><li>My Account</li><li>Register</li><li>Checkout</li><li class="login">Log In</li>
  </ul>
</div>

<!-- header -->
<header class="abs header">
  <div class="brand"><div class="name">CURL</div><div class="tag">RADIANT THROUGH &amp; THROUGH</div></div>
  <div class="search"><div class="field"></div><div class="btn">SEARCH</div></div>
</header>

<nav class="abs nav">
  <ul>
    <li class="active">HOME</li><li>BROWSE PHOTOS</li><li>HOW IT WORKS</li><li>LOCATION</li><li>CONTACT US</li><li>GALLERY</li><li>POLICY</li><li>FAQS</li>
  </ul>
</nav>

<!-- hero -->
<section class="abs hero" role="img" aria-label="Portrait of a woman with a sleek styled ponytail">
  <div class="rule"></div>
  <div class="caption">THIS IS THE LAST SLIDE</div>
  <div class="arrow" style="left:132px"><svg width="12" height="16"><polyline points="9,2 3,8 9,14" fill="none" stroke="#fff" stroke-width="1.5"/></svg></div>
  <div class="arrow" style="left:183px"><svg width="12" height="16"><polyline points="3,2 9,8 3,14" fill="none" stroke="#fff" stroke-width="1.5"/></svg></div>
  <svg class="abs" style="left:898px;top:40px" width="168" height="40"><polyline points="2,38 84,4 166,38" fill="none" stroke="#9a8f86" stroke-width="1"/><circle cx="84" cy="4" r="3" fill="#ccc"/></svg>
  <div class="hours">
    <h3>OPENING TIME</h3>
    <table>
      <tr><td>Monday</td><td>9:00-18:00</td></tr>
      <tr><td>Tuesday</td><td>9:00-18:00</td></tr>
      <tr><td>Wednesday</td><td>8:00-18:00</td></tr>
      <tr class="today"><td>Thursday</td><td>9:00-18:00</td></tr>
      <tr><td>Friday</td><td>9:00-18:00</td></tr>
      <tr><td>Saturday</td><td>9:00-18:00</td></tr>
      <tr class="closed"><td>Sunday</td><td>CLOSED</td></tr>
    </table>
  </div>
</section>

<!-- about -->
<section class="abs about">
  <div class="abs section-title" style="left:-132px;top:20px;width:1200px"><svg width="36" height="36"><use href="#scissors"/></svg>ABOUT US<svg width="36" height="36"><use href="#scissors"/></svg></div>
  <h2>CURL RADIANT THROUGH &amp; THROUGH BY MARISOL B.</h2>
  <p>Creative. Classic. Distinguished. These are just a few attributes that Marisol embodies. received in depth training from Brightwater Academy of Hair Design, where I had the opportunity to pair my experience with advanced technical training. My passion for art and design has given me the opportunity to express myself through hair design. I also stay abreast of current trends through industry events, hair shows, and continuing education so that I can offer my clients the best services in hair care, style, and extensions.<br>I've spent the last five years perfecting my method of installing extensions which offers my clients a flawless look while maintaining healthy Fusion I-tips, and Micro beaded I-tip extensions.</p>
  <div class="abs btn-gold" style="left:237px;top:316px;width:200px;height:40px">Book an Appointment</div>
  <div class="abs portrait" role="img" aria-label="Portrait of the stylist beside her handwritten signature" style="background:linear-gradient(90deg,#c99a6a 0%,#3a2e2a 45%,#fff 70%,#f6f6f6 100%)"></div>
  <div class="abs btn-gold" style="left:668px;top:354px;width:108px;height:30px;font-size:13px">Massage Me</div>
  <div class="abs btn-gold" style="left:800px;top:354px;width:108px;height:30px;font-size:13px">Contact Info</div>
</section>

<!-- gallery -->
<div class="abs section-title" style="top:1018px"><svg width="36" height="36"><use href="#scissors"/></svg>GALLERY<svg width="36" height="36"><use href="#scissors"/></svg></div>

<div class="photo" role="img" aria-label="Hair being blow-dried" style="left:132px;top:1076px;width:294px;height:185px;background:linear-gradient(135deg,#b9c4d6,#7e8796 60%,#d0d6e0);border:6px solid #c9d4e8">
  <svg class="abs" style="left:128px;top:74px" width="26" height="26"><line x1="13" y1="0" x2="13" y2="26" stroke="#fff" stroke-width="3"/><line x1="0" y1="13" x2="26" y2="13" stroke="#fff" stroke-width="3"/></svg>
</div>
<div class="photo" role="img" aria-label="Smiling woman with long wavy hair" style="left:451px;top:1076px;width:296px;height:201px;background:linear-gradient(135deg,#8c9a72,#c99a70 50%,#e9d9c5)"></div>
<div class="photo" role="img" aria-label="Woman with soft makeup and blonde waves" style="left:772px;top:1076px;width:294px;height:185px;background:linear-gradient(135deg,#d9cbc2,#9a7a66 55%,#c4b4a8)"></div>

<div class="photo" role="img" aria-label="Black and white portrait of a woman with flowing hair" style="left:132px;top:1286px;width:294px;height:185px;background:linear-gradient(135deg,#8a8a8a,#dcdcdc 45%,#4a4a4a)"></div>
<div class="photo" role="img" aria-label="Long glossy auburn hair" style="left:451px;top:1301px;width:296px;height:186px;background:linear-gradient(160deg,#fafafa 10%,#8c3a22 45%,#5a2418 75%,#fafafa)"></div>
<div class="photo" role="img" aria-label="Woman with curly hair and sunglasses" style="left:772px;top:1286px;width:294px;height:185px;background:linear-gradient(135deg,#eee3d6,#b8704a 55%,#e8dccd)"></div>

<div class="photo" role="img" aria-label="Woman with bangs and a side braid outdoors" style="left:132px;top:1494px;width:294px;height:243px;background:linear-gradient(135deg,#a9cf7a,#dbe9bf 40%,#5a3a2a 70%,#e6e2d8)"></div>
<div class="photo" role="img" aria-label="Woman with red curls and dramatic makeup" style="left:451px;top:1512px;width:296px;height:185px;background:linear-gradient(135deg,#0e1628,#8a3a1e 45%,#d98a58 70%,#141a2a)"></div>
<div class="photo" role="img" aria-label="Woman with voluminous brown hair covering her face" style="left:772px;top:1494px;width:294px;height:243px;background:linear-gradient(135deg,#6a3a24,#a8653a 45%,#3a1e14)"></div>

<div class="abs btn-gold" style="left:535px;top:1722px;width:130px;height:35px;font-size:16px">View More</div>

<!-- our work -->
<div class="abs section-title" style="top:1797px"><svg width="36" height="36"><use href="#scissors"/></svg>OUR WORK<svg width="36" height="36"><use href="#scissors"/></svg></div>
<div class="abs tabs"><span class="active">BASIC SERVICES</span><span>COLOR SERVICES</span><span>EXTENSIONS</span><span>STRAITENING SERVICES</span></div>

<div class="abs service-box">
  <h4>BASIC SERVICES</h4>
  <p>Lorem Ipsum is simply dummy text of the printing.</p>
  <span class="book">Book Now</span>
</div>
<div class="abs work-card" role="img" aria-label="Man receiving a haircut" style="left:371px;background:linear-gradient(135deg,#efe9e1,#c8a88a 55%,#f2eee8)"></div>
<div class="abs work-card" role="img" aria-label="Woman having curls styled with hairspray" style="left:612px;background:linear-gradient(135deg,#f2ede6,#5a3e30 55%,#ede6dc)"></div>
<div class="abs work-card" role="img" aria-label="Stylist combing long blonde hair" style="left:852px;background:linear-gradient(135deg,#f1ece4,#d9b884 55%,#efe8dc)"></div>

<!-- testimonial -->
<section class="abs testimonial" role="img" aria-label="Faded portrait of a woman behind the testimonial">
  <div class="abs section-title" style="left:0;top:24px;width:934px"><svg width="36" height="36"><use href="#scissors-light"/></svg>TESTIMONIAL<svg width="36" height="36"><use href="#scissors-light"/></svg></div>
  <div class="lead">We Make Beauty</div>
  <div class="quote">"I have been looking for a stylist since I moved to Dallas for 7 years. I noticed a young ladys hair and she gave me Marisol information. I LOVE MY HAIR. She does an amazing job. Always leave satisfied!!!"</div>
  <div class="author"><div class="avatar" role="img" aria-label="Client photo"></div><span>Renata V.</span></div>
  <div class="dots"><span></span><span></span></div>
</section>

<!-- footer -->
<footer class="abs footer">
  <h5 class="gold" style="left:132px">Location</h5>
  <div class="abs" role="img" aria-label="Street map of the salon location" style="left:132px;top:57px;width:204px;height:140px;background:#e4e2dc">
    <svg class="abs" style="left:92px;top:30px" width="24" height="34"><path d="M12 33 C4 20 1 15 1 11 A11 11 0 0 1 23 11 C23 15 20 20 12 33Z" fill="#d23a3a"/><circle cx="12" cy="11" r="4" fill="#fff"/></svg>
  </div>

  <h5 style="left:371px">Our Address</h5>
  <ul class="contact" style="left:371px;top:54px">
    <li><span class="ic pin"><svg width="10" height="12"><path d="M5 12 C1 7 0 5 0 4 A5 4 0 0 1 10 4 C10 5 9 7 5 12Z" fill="#fff"/></svg></span><span>Curl R.T.T. By Marisol B. @ Lumen Salon Suites</span></li>
    <li><span class="ic"><svg width="10" height="10"><path d="M1 1 L4 1 L5 3 L3 4 Q4 6 6 7 L7 5 L9 6 L9 9 Q3 9 1 1Z" fill="#ccc"/></svg></span><span style="padding-top:5px">Phone: 555-014-2266</span></li>
    <li><span class="ic"><svg width="12" height="9"><rect x="0.5" y="0.5" width="11" height="8" fill="none" stroke="#ccc"/><polyline points="0.5,0.5 6,5 11.5,0.5" fill="none" stroke="#ccc"/></svg></span><span style="padding-top:5px">Email: info@trimnook.example</span></li>
  </ul>

  <h5 style="left:612px">Connect With Us</h5>
  <ul class="social" style="left:612px;top:54px">
    <li><span class="ic"></span>Friendwall</li>
    <li><span class="ic"></span>Chirpline</li>
    <li><span class="ic"></span>Circleplus</li>
    <li><span class="ic"></span>Workweave</li>
  </ul>

  <h5 style="left:852px">Media</h5>
  <ul class="media" style="left:852px;top:54px">
    <li>Beauty Blog</li><li>Press</li><li>Stories</li><li>Videos</li><li>Services</li>
  </ul>

  <div class="copyright">Copyright © 2016 curlradiantthroughandthrough.example. All rights reserved.</div>
  <div class="pay" style="left:879px">quick fund</div>
  <div class="pay" style="left:927px">Vistacard</div>
  <div class="pay" style="left:975px">Amerivault</div>
  <div class="pay" style="left:1023px">Maxcard</div>
</footer>

</body>
</html>
```